Review/Re-Design Supermarket E-Commerce website

We have launched our Supermarket E-commerce Website but feel it is lacking a modern feel.

Please re-design the current Supermarket E-commerce site, creating a more modern look and feel.

I am looking for design changes to things such as:

- Fonts
- Button shape & Size
- Shapes of boxes
- Layout of drop down menus
- A new shopping cart / button
- The Header (and in particular the use and positioning of the logo)
- Supplying a generic background image (currently berries)

Please do not change the structure of the page. For instance, the category selection will always be on the left, the items will always be displayed in rows of 3 and the shopping cart should be on the right.
Updates

Current site can be found at www.brovanmarket.com.au

Project Deadline Extended
Reason: designs coming in are generally too different from current design. we are looking for less that 10% change to the overall look and feel. one aspect that needs a lot of work is the checkout cart on the right hand side. please checkout http://www2.pelkinfreshmart.com.au/?gclid=QXRP4kdmwnLBHTYEzJuaPGEKtB

Target Market(s)

Consumers buying their weekly grocery shopping online

Industry/Entity Type

Shopping

Number of Pages Required

1 page

Requirements
Must have
• Stick to the branding of the Logo. Which is Red, Blue and White.
• Other colours may be used in small percentages.
Should not have
• Do not change the Structure of the site.

```html
<!DOCTYPE html>
<html lang="en">
<head>
<meta charset="utf-8">
<title>Brovan Market – Online Grocery</title>
<link href="https://fonts.googleapis.com/css2?family=Open+Sans:wght@400;600;700&family=Oswald:wght@500;700&family=Pacifico&display=swap" rel="stylesheet">
<style>
:root{
  --red:#e23a2c;
  --red-dark:#c22a1e;
  --blue:#1f4f9e;
  --green:#5fb84a;
  --green-soft:#e6f4df;
  --teal:#3bb39a;
  --orange:#f39a2c;
  --brown:#6a4a38;
  --ink:#333;
  --muted:#888;
  --line:#e6e6e6;
  --dark:#2b2b2b;
  --darker:#1e1e1e;
  --bg:#ffffff;
  --paper:#f6f6f6;
}
*{box-sizing:border-box;margin:0;padding:0}
html,body{width:1200px;height:3888px;overflow:hidden}
body{font-family:"Open Sans",Arial,sans-serif;color:var(--ink);background:var(--bg);font-size:12px;position:relative}
.wrap{position:absolute;left:100px;width:1000px}

/* top bar */
.topbar{top:0;height:38px;display:flex;align-items:center;justify-content:space-between;font-size:11px;color:var(--muted);border-bottom:1px solid var(--line)}
.topbar a{color:var(--muted);text-decoration:none;margin-left:14px}

/* header */
.header{top:38px;height:88px;display:flex;align-items:center}
.brand{display:flex;align-items:center;gap:10px;width:250px}
.brand-dot{width:34px;height:34px;border-radius:50%;background:var(--red)}
.brand-name{font-family:"Oswald",sans-serif;font-weight:700;font-size:22px;color:var(--blue);letter-spacing:.5px}
.head-main{flex:1}
.nav{display:flex;gap:28px;font-family:"Oswald",sans-serif;font-weight:500;font-size:13px;color:var(--dark);letter-spacing:.5px}
.nav span.caret:after{content:" ▾";font-size:9px;color:var(--muted)}
.search{margin-top:12px;display:flex;height:32px;width:560px;border:1px solid var(--line)}
.search .cat{width:130px;border-right:1px solid var(--line);padding:0 10px;display:flex;align-items:center;color:var(--muted);font-size:11px}
.search .field{flex:1;padding:0 10px;display:flex;align-items:center;color:#bbb;font-size:11px}
.search .go{width:40px;background:var(--red);display:flex;align-items:center;justify-content:center}
.cart{width:130px;height:36px;background:var(--red);color:#fff;border-radius:3px;display:flex;align-items:center;justify-content:center;gap:8px;font-weight:700;font-size:11px;letter-spacing:.5px}

/* mega menu */
.mega{top:150px;height:560px;left:100px;width:240px;background:var(--dark);position:absolute}
.mega-title{height:44px;background:var(--red);color:#fff;font-family:"Oswald",sans-serif;font-size:14px;display:flex;align-items:center;padding:0 16px;gap:10px;letter-spacing:.5px}
.mega ul{list-style:none}
.mega li{height:33px;border-bottom:1px solid #3a3a3a;color:#ccc;font-size:11px;display:flex;align-items:center;padding:0 16px;gap:10px;text-transform:uppercase}
.mega li:before{content:"";width:8px;height:8px;border:1px solid #777}

/* hero */
.hero{position:absolute;top:150px;left:356px;width:494px;height:356px;background:linear-gradient(135deg,#f5c93b,#f2b421)}
.hero-photo{position:absolute;left:20px;top:40px;width:210px;height:280px;background:linear-gradient(#d8d8d8,#9a9a9a);border-radius:4px}
.hero-copy{position:absolute;right:30px;top:120px;text-align:center;color:#fff}
.hero-copy .small{font-size:13px;letter-spacing:2px;font-weight:600;color:#5a3b10}
.hero-copy .big{font-family:"Oswald",sans-serif;font-size:44px;font-weight:700;line-height:1;margin-top:6px}
.side-banner{position:absolute;left:866px;width:234px}
.b-citrus{top:150px;height:238px;background:linear-gradient(160deg,#ffb347,#f57c1f)}
.b-menu{top:404px;height:306px;background:linear-gradient(#6cc457,#4aa93a)}
.side-banner .label{position:absolute;left:16px;top:18px;color:#fff;font-family:"Pacifico",cursive;font-size:24px;line-height:1.1}
.side-banner .ph{position:absolute;left:20px;right:20px;bottom:20px;height:120px;border-radius:4px}
.b-citrus .ph{background:linear-gradient(#fbd14b,#ee5a2a)}
.b-menu .ph{background:linear-gradient(#e9a35a,#b5642b);height:160px}
.b-menu .label{font-family:"Open Sans",sans-serif;font-size:15px;font-weight:700}

.bestseller{position:absolute;top:510px;left:356px;width:494px;height:200px;border:1px solid var(--line)}
.bestseller h3{height:26px;background:var(--green);color:#fff;font-size:11px;font-family:"Oswald",sans-serif;display:flex;align-items:center;justify-content:center;letter-spacing:1px}
.best-row{display:flex}
.best-row .item{flex:1;padding:10px;border-right:1px solid var(--line)}
.best-row .item:last-child{border:none}
.best-row .thumb{height:90px;margin-top:8px;border-radius:3px}

/* features */
.features{top:730px;height:60px;display:flex;border:1px solid var(--line)}
.feature{flex:1;display:flex;align-items:center;gap:12px;padding:0 18px;border-right:1px solid var(--line)}
.feature:last-child{border:none}
.feature b{display:block;font-size:11px;color:var(--dark)}
.feature small{font-size:10px;color:var(--muted)}

/* product sections */
.section{position:absolute;left:100px;width:1000px;height:500px}
.sec-head{height:40px;display:flex;align-items:center;border-bottom:2px solid var(--line)}
.sec-title{font-family:"Oswald",sans-serif;font-size:20px;font-weight:500;padding-right:20px}
.tabs{margin-left:auto;display:flex;gap:16px;font-size:10px;color:var(--muted)}
.tabs span:first-child{color:var(--dark);font-weight:600}
.tag{height:40px;display:flex;align-items:center;padding:0 14px;color:#fff;font-family:"Oswald",sans-serif;font-size:13px;letter-spacing:.5px}
.sec-body{display:flex;height:460px}
.grid{width:500px;display:grid;grid-template-columns:repeat(3,1fr);grid-template-rows:repeat(2,1fr);border-left:1px solid var(--line)}
.card{border-right:1px solid var(--line);border-bottom:1px solid var(--line);padding:10px 12px;position:relative}
.card .name{font-size:10.5px;color:var(--dark);height:28px;line-height:14px}
.card .stars{color:#f5b400;font-size:9px;letter-spacing:1px}
.card .price{font-size:12px;font-weight:700;color:var(--red)}
.card .price s{color:#aaa;font-weight:400;font-size:10px;margin-left:4px}
.card .pimg{height:120px;margin-top:8px;border-radius:3px}
.badge{position:absolute;right:12px;top:100px;width:30px;height:30px;border-radius:50%;background:var(--green);color:#fff;font-size:9px;font-weight:700;display:flex;align-items:center;justify-content:center}
.promo{width:250px;position:relative;overflow:hidden}
.promo .ph{position:absolute;left:30px;right:30px;bottom:30px;height:220px;border-radius:4px}
.promo .pt{position:absolute;left:0;right:0;top:40px;text-align:center;color:#fff;font-family:"Oswald",sans-serif}
.promo .pt .a{font-size:14px;letter-spacing:1px}
.promo .pt .b{font-size:30px;font-weight:700;line-height:1.1}
.promo .pt .c{font-size:12px;margin-top:6px;font-family:"Open Sans",sans-serif}
.list{width:250px;border:1px solid var(--line);border-top:none}
.list .li{height:114px;display:flex;gap:10px;padding:12px;border-bottom:1px solid var(--line)}
.list .li:last-child{border:none}
.list .th{width:80px;height:80px;border-radius:3px;flex:none}
.list .li .name{font-size:10.5px;color:var(--dark);margin-bottom:4px}
.list .li .price{font-size:12px;font-weight:700;color:var(--red);margin-top:4px}
.head-split{display:flex}

/* brand strip */
.strip{top:3530px;height:80px;display:flex;align-items:center;justify-content:space-around;border:1px solid var(--line)}
.strip .mini{display:flex;align-items:center;gap:8px;font-family:"Oswald",sans-serif;font-weight:700;color:var(--blue);font-size:16px}
.strip .mini i{width:20px;height:20px;border-radius:50%;background:var(--red)}
.arrow{font-size:16px;color:#bbb}

/* newsletter & footer */
.newsletter{position:absolute;top:3640px;left:0;width:1200px;height:60px;background:var(--dark);display:flex;align-items:center;justify-content:center;gap:20px}
.newsletter b{color:#fff;font-family:"Oswald",sans-serif;font-size:14px;letter-spacing:1px}
.newsletter .in{width:300px;height:32px;background:#fff;color:#aaa;font-size:11px;display:flex;align-items:center;padding:0 10px}
.newsletter .btn{height:32px;padding:0 18px;background:var(--red);color:#fff;font-size:11px;font-weight:700;display:flex;align-items:center}
.footer{position:absolute;top:3700px;left:0;width:1200px;height:188px;background:var(--darker);color:#999}
.footer .cols{position:absolute;left:100px;width:1000px;top:26px;display:flex}
.footer .col{flex:1;font-size:10.5px;line-height:20px}
.footer h4{color:#fff;font-size:11px;margin-bottom:8px;letter-spacing:.5px}
.foot-brand{display:flex;align-items:center;gap:8px;background:#fff;padding:8px 10px;width:200px;margin-bottom:10px}
.foot-brand i{width:20px;height:20px;border-radius:50%;background:var(--red)}
.foot-brand span{font-family:"Oswald",sans-serif;font-weight:700;color:var(--blue);font-size:15px}

.social{position:absolute;right:10px;top:140px;display:flex;flex-direction:column;gap:4px}
.social i{width:34px;height:34px}
.totop{position:absolute;right:96px;top:1780px;width:24px;height:40px;background:#ddd}
</style>
</head>
<body>

<div class="wrap topbar">
  <span>Welcome to www.brovanmarket.com.au</span>
  <span><a>My Account</a><a>Wishlist</a><a>Checkout</a><a>Login</a></span>
</div>

<header class="wrap header">
  <div class="brand"><i class="brand-dot"></i><span class="brand-name">BROVAN MARKET</span></div>
  <div class="head-main">
    <nav class="nav"><span>HOME</span><span class="caret">BRANDS</span><span class="caret">FRUIT</span><span class="caret">IMPORTED FOOD</span><span class="caret">BLOG</span><span>CONTACT</span></nav>
    <div class="search"><div class="cat">All Categories ▾</div><div class="field">Search entire store...</div><div class="go"><svg width="14" height="14" viewBox="0 0 14 14"><circle cx="6" cy="6" r="4.5" fill="none" stroke="#fff" stroke-width="1.8"/><line x1="9.5" y1="9.5" x2="13" y2="13" stroke="#fff" stroke-width="1.8"/></svg></div></div>
  </div>
  <div class="cart"><svg width="16" height="14" viewBox="0 0 16 14"><path d="M1 1h2.5l2 8h8l1.5-6H4.5" fill="none" stroke="#fff" stroke-width="1.6"/><circle cx="6.5" cy="12" r="1.3" fill="#fff"/><circle cx="12.5" cy="12" r="1.3" fill="#fff"/></svg>MY CART · 0 ITEM</div>
</header>

<aside class="mega">
  <div class="mega-title">☰ VERTICAL MEGAMENU</div>
  <ul>
    <li>Fruit &amp; Veg</li><li>Meat &amp; Seafood</li><li>Dairy &amp; Eggs</li><li>Bakery</li><li>Pantry</li><li>Frozen</li><li>Drinks</li><li>Snacks</li><li>Baby Care</li><li>Health</li><li>Household</li><li>Pet Food</li><li>Cleaning</li><li>Liquor</li><li>Deli</li>
  </ul>
</aside>

<div class="hero">
  <div class="hero-photo" role="img" aria-label="Stainless kitchen appliances: fridge, oven and microwave"></div>
  <div class="hero-copy"><div class="small">DELIGHT YOUR</div><div class="big">TASTEBUDS</div></div>
</div>
<div class="side-banner b-citrus"><div class="label">Fresh fruit<br>Citrus</div><div class="ph" role="img" aria-label="Sliced oranges and grapefruit"></div></div>
<div class="side-banner b-menu"><div class="label">The menu you love<br>Plus smoothie</div><div class="ph" role="img" aria-label="Burger and drink meal"></div></div>

<div class="bestseller">
  <h3>BEST SELLER</h3>
  <div class="best-row">
    <div class="item"><div class="card-name">Lorem ipsum dolor</div><div class="stars">★★★★★</div><div class="thumb" role="img" aria-label="Packaged snack" style="background:linear-gradient(#f0d8a8,#c99a55)"></div></div>
    <div class="item"><div class="card-name">Maecenas ultricies</div><div class="stars">★★★★★</div><div class="thumb" role="img" aria-label="Fresh vegetables" style="background:linear-gradient(#b9e08a,#5aa33a)"></div></div>
    <div class="item"><div class="card-name">Integer velit mauris</div><div class="stars">★★★★★</div><div class="thumb" role="img" aria-label="Fruit juice bottles" style="background:linear-gradient(#ffd27a,#e98a2a)"></div></div>
  </div>
</div>

<div class="wrap features">
  <div class="feature"><svg width="26" height="18"><rect x="1" y="3" width="15" height="11" fill="none" stroke="#555"/><path d="M16 6h5l4 4v4h-9" fill="none" stroke="#555"/></svg><div><b>Free Shipping</b><small>On orders over $99</small></div></div>
  <div class="feature"><svg width="22" height="22"><circle cx="11" cy="11" r="9" fill="none" stroke="#555"/><path d="M11 5v6l4 3" fill="none" stroke="#555"/></svg><div><b>30 Months Warranty</b><small>Shop in peace of mind</small></div></div>
  <div class="feature"><svg width="22" height="22"><rect x="2" y="6" width="18" height="14" fill="none" stroke="#555"/><path d="M2 10h18M11 6v14" stroke="#555"/></svg><div><b>Gifts &amp; Offers</b><small>Save more every week</small></div></div>
  <div class="feature"><svg width="22" height="22"><path d="M4 11l5 5 9-10" fill="none" stroke="#555" stroke-width="2"/></svg><div><b>Best Price Guarantee</b><small>Lowest prices in town</small></div></div>
</div>

<!-- Delicious Snacks -->
<section class="section" style="top:830px">
  <div class="head-split">
    <div class="sec-head" style="width:750px"><span class="sec-title" style="color:var(--green)">Delicious Snacks</span><div class="tabs"><span>Home</span><span>Chips</span><span>Nuts</span><span>Biscuits</span><span>Sweets</span><span>Crackers</span></div></div>
    <div class="tag" style="width:250px;background:var(--green)">SPECIAL PRODUCTS</div>
  </div>
  <div class="sec-body">
    <div class="grid">
      <div class="card"><div class="name">Lorem ipsum dolor sit amet</div><div class="stars">★★★★★</div><div class="price">$55.00<s>$60.00</s></div><div class="pimg" role="img" aria-label="Bag of mixed nuts" style="background:linear-gradient(#e9cf8f,#b98a3d)"></div><span class="badge">NEW</span></div>
      <div class="card"><div class="name">Donec rutrum lorem nec pretium</div><div class="stars">★★★★★</div><div class="price">$48.00</div><div class="pimg" role="img" aria-label="Bowl of pistachios" style="background:linear-gradient(#dfe2b0,#9aa05a)"></div><span class="badge">NEW</span></div>
      <div class="card"><div class="name">Integer velit mauris</div><div class="stars">★★★★★</div><div class="price">$40.00</div><div class="pimg" role="img" aria-label="Cashew nuts" style="background:linear-gradient(#f1dfb8,#cda46a)"></div><span class="badge">NEW</span></div>
      <div class="card"><div class="name">Nam vulputate magna</div><div class="stars">★★★★★</div><div class="price">$70.00<s>$78.00</s></div><div class="pimg" role="img" aria-label="Walnuts" style="background:linear-gradient(#d3b58a,#8c6438)"></div><span class="badge">NEW</span></div>
      <div class="card"><div class="name">Maecenas ultricies</div><div class="stars">★★★★★</div><div class="price">$40.00</div><div class="pimg" role="img" aria-label="Peanuts in shell" style="background:linear-gradient(#e8cf9c,#b58a4e)"></div><span class="badge">NEW</span></div>
      <div class="card"><div class="name">Curabitur tristique</div><div class="stars">★★★★★</div><div class="price">$62.00</div><div class="pimg" role="img" aria-label="Pistachios" style="background:linear-gradient(#e3e4b9,#a5a760)"></div><span class="badge">NEW</span></div>
    </div>
    <div class="promo" style="background:linear-gradient(#8fd36a,#5fb84a)">
      <div class="pt"><div class="a">MACADAMIA</div><div class="b">SAVE UP 75% OFF</div><div class="c">On selected products</div></div>
      <div class="ph" role="img" aria-label="Bag of macadamia nuts" style="background:linear-gradient(#f3e6c7,#c9a56a)"></div>
    </div>
    <div class="list">
      <div class="li"><div class="th" role="img" aria-label="Snack pack" style="background:linear-gradient(#f0d8a8,#c99a55)"></div><div><div class="name">Integer velit mauris</div><div class="stars">★★★★★</div><div class="price">$50.00</div></div></div>
      <div class="li"><div class="th" role="img" aria-label="Dried fruit" style="background:linear-gradient(#e6b58a,#a86838)"></div><div><div class="name">Curabitur tristique</div><div class="stars">★★★★★</div><div class="price">$45.00</div></div></div>
      <div class="li"><div class="th" role="img" aria-label="Almonds" style="background:linear-gradient(#e2c49a,#a67c48)"></div><div><div class="name">Nam vulputate magna</div><div class="stars">★★★★★</div><div class="price">$39.00</div></div></div>
      <div class="li"><div class="th" role="img" aria-label="Trail mix" style="background:linear-gradient(#ead09c,#b48a4a)"></div><div><div class="name">Maecenas ultricies</div><div class="stars">★★★★★</div><div class="price">$58.00</div></div></div>
    </div>
  </div>
</section>

<!-- Fresh Fruit -->
<section class="section" style="top:1370px">
  <div class="head-split">
    <div class="tag" style="width:250px;background:var(--red)">NEW PRODUCTS</div>
    <div class="sec-head" style="width:750px;padding-left:16px"><span class="sec-title" style="color:var(--red)">Fresh Fruit</span><div class="tabs"><span>Home</span><span>Apples</span><span>Berries</span><span>Citrus</span><span>Tropical</span><span>Stone</span></div></div>
  </div>
  <div class="sec-body">
    <div class="list">
      <div class="li"><div class="th" role="img" aria-label="Raspberries" style="background:linear-gradient(#f27a7a,#b8232e)"></div><div><div class="name">Nam vulputate magna</div><div class="stars">★★★★★</div><div class="price">$20.00</div></div></div>
      <div class="li"><div class="th" role="img" aria-label="Lemons" style="background:linear-gradient(#fff09a,#e8c52a)"></div><div><div class="name">Maecenas ultricies</div><div class="stars">★★★★★</div><div class="price">$15.00</div></div></div>
      <div class="li"><div class="th" role="img" aria-label="Strawberries" style="background:linear-gradient(#f48a8a,#c62b2b)"></div><div><div class="name">Curabitur tristique</div><div class="stars">★★★★★</div><div class="price">$18.00</div></div></div>
      <div class="li"><div class="th" role="img" aria-label="Cherries" style="background:linear-gradient(#c84a5a,#7a1424)"></div><div><div class="name">Integer velit mauris</div><div class="stars">★★★★★</div><div class="price">$24.00</div></div></div>
    </div>
    <div class="promo" style="background:linear-gradient(#ffad4a,#f0811e)">
      <div class="pt"><div class="a">OUR FRESH &amp; TASTY</div><div class="b">FRUITS</div><div class="c">&amp; vegetables · Save 30%</div></div>
      <div class="ph" role="img" aria-label="Basket of oranges" style="background:linear-gradient(#ffc04a,#e4721a)"></div>
    </div>
    <div class="grid">
      <div class="card"><div class="name">Aelia facilisis</div><div class="stars">★★★★★</div><div class="price">$22.00</div><div class="pimg" role="img" aria-label="Kiwi fruit" style="background:linear-gradient(#b8d67a,#6a8a2a)"></div><span class="badge">NEW</span></div>
      <div class="card"><div class="name">Aliquam ac lectus</div><div class="stars">★★★★★</div><div class="price">$19.00</div><div class="pimg" role="img" aria-label="Strawberries" style="background:linear-gradient(#f48a8a,#c62b2b)"></div><span class="badge">NEW</span></div>
      <div class="card"><div class="name">Etiam non auctor</div><div class="stars">★★★★★</div><div class="price">$26.00</div><div class="pimg" role="img" aria-label="Peaches" style="background:linear-gradient(#ffc58a,#e2683a)"></div><span class="badge">NEW</span></div>
      <div class="card"><div class="name">Integer velit mauris</div><div class="stars">★★★★★</div><div class="price">$30.00</div><div class="pimg" role="img" aria-label="Blueberries" style="background:linear-gradient(#7a86c8,#2c3478)"></div><span class="badge">NEW</span></div>
      <div class="card"><div class="name">Etiam non auctor</div><div class="stars">★★★★★</div><div class="price">$17.00</div><div class="pimg" role="img" aria-label="Sliced fruit" style="background:linear-gradient(#f6e2a0,#d6843a)"></div><span class="badge">NEW</span></div>
      <div class="card"><div class="name">Aliquam ac lectus</div><div class="stars">★★★★★</div><div class="price">$21.00</div><div class="pimg" role="img" aria-label="Cherries" style="background:linear-gradient(#d25a6a,#7a1424)"></div><span class="badge">NEW</span></div>
    </div>
  </div>
</section>

<!-- Imported Food -->
<section class="section" style="top:1910px">
  <div class="head-split">
    <div class="sec-head" style="width:750px"><span class="sec-title" style="color:var(--teal)">Imported Food</span><div class="tabs"><span>Home</span><span>Asian</span><span>Italian</span><span>Sweets</span><span>Sauces</span></div></div>
    <div class="tag" style="width:250px;background:var(--teal)">SPECIAL PRODUCTS</div>
  </div>
  <div class="sec-body">
    <div class="grid">
      <div class="card"><div class="name">Nam vulputate magna</div><div class="stars">★★★★★</div><div class="price">$12.00</div><div class="pimg" role="img" aria-label="Boxed crackers" style="background:linear-gradient(#8fb8e8,#e05a3a)"></div><span class="badge">NEW</span></div>
      <div class="card"><div class="name">Lorem ipsum dolor</div><div class="stars">★★★★★</div><div class="price">$9.00</div><div class="pimg" role="img" aria-label="Candy packets" style="background:linear-gradient(#f4a6c6,#6ac0d8)"></div><span class="badge">NEW</span></div>
      <div class="card"><div class="name">Maecenas ultricies</div><div class="stars">★★★★★</div><div class="price">$14.00</div><div class="pimg" role="img" aria-label="Imported biscuits" style="background:linear-gradient(#e8d08a,#b88a3a)"></div><span class="badge">NEW</span></div>
      <div class="card"><div class="name">Curabitur tristique</div><div class="stars">★★★★★</div><div class="price">$11.00</div><div class="pimg" role="img" aria-label="Snack bags" style="background:linear-gradient(#f8d86a,#e06a2a)"></div><span class="badge">NEW</span></div>
      <div class="card"><div class="name">Integer velit mauris</div><div class="stars">★★★★★</div><div class="price">$16.00</div><div class="pimg" role="img" aria-label="Chocolate boxes" style="background:linear-gradient(#a8704a,#5a3218)"></div><span class="badge">NEW</span></div>
      <div class="card"><div class="name">Etiam non auctor</div><div class="stars">★★★★★</div><div class="price">$13.00</div><div class="pimg" role="img" aria-label="Wafer packs" style="background:linear-gradient(#f6e06a,#d84a2a)"></div><span class="badge">NEW</span></div>
    </div>
    <div class="promo" style="background:linear-gradient(#5fcab2,#2f9f88)">
      <div class="pt"><div class="a">IMPORTED</div><div class="b">PRODUCTS</div><div class="c">Save up to 50% off</div></div>
      <div class="ph" role="img" aria-label="Chocolate bars" style="background:linear-gradient(#b07a52,#5a2e18)"></div>
    </div>
    <div class="list">
      <div class="li"><div class="th" role="img" aria-label="Cereal box" style="background:linear-gradient(#f0b46a,#c0522a)"></div><div><div class="name">Nam vulputate magna</div><div class="stars">★★★★★</div><div class="price">$10.00</div></div></div>
      <div class="li"><div class="th" role="img" aria-label="Candy pack" style="background:linear-gradient(#f4a6c6,#c24a8a)"></div><div><div class="name">Maecenas ultricies</div><div class="stars">★★★★★</div><div class="price">$8.00</div></div></div>
      <div class="li"><div class="th" role="img" aria-label="Biscuit tin" style="background:linear-gradient(#8ab8e8,#2a5a9e)"></div><div><div class="name">Curabitur tristique</div><div class="stars">★★★★★</div><div class="price">$15.00</div></div></div>
      <div class="li"><div class="th" role="img" aria-label="Snack bag" style="background:linear-gradient(#f8d86a,#e06a2a)"></div><div><div class="name">Integer velit mauris</div><div class="stars">★★★★★</div><div class="price">$7.00</div></div></div>
    </div>
  </div>
</section>

<!-- Beverage -->
<section class="section" style="top:2450px">
  <div class="head-split">
    <div class="tag" style="width:250px;background:var(--red)">NEW PRODUCTS</div>
    <div class="sec-head" style="width:750px;padding-left:16px"><span class="sec-title" style="color:var(--red)">Beverage</span><div class="tabs"><span>Home</span><span>Water</span><span>Juice</span><span>Soda</span><span>Coffee</span><span>Tea</span></div></div>
  </div>
  <div class="sec-body">
    <div class="list">
      <div class="li"><div class="th" role="img" aria-label="Juice bottles" style="background:linear-gradient(#ffd27a,#e98a2a)"></div><div><div class="name">Maecenas ultricies</div><div class="stars">★★★★★</div><div class="price">$6.00</div></div></div>
      <div class="li"><div class="th" role="img" aria-label="Soft drink cans" style="background:linear-gradient(#f2e27a,#d8a22a)"></div><div><div class="name">Integer velit mauris</div><div class="stars">★★★★★</div><div class="price">$5.00</div></div></div>
      <div class="li"><div class="th" role="img" aria-label="Iced tea bottles" style="background:linear-gradient(#f4b07a,#c0522a)"></div><div><div class="name">Nam vulputate magna</div><div class="stars">★★★★★</div><div class="price">$4.00</div></div></div>
      <div class="li"><div class="th" role="img" aria-label="Sauce bottles" style="background:linear-gradient(#f09a6a,#b0321e)"></div><div><div class="name">Curabitur tristique</div><div class="stars">★★★★★</div><div class="price">$7.00</div></div></div>
    </div>
    <div class="promo" style="background:linear-gradient(#8ed872,#4fae3c)">
      <div class="pt"><div class="a">BEVERAGE</div><div class="b">SAVE UP TO<br>30% OFF</div></div>
      <div class="ph" role="img" aria-label="Glass of mojito with lime and mint" style="background:linear-gradient(#e8f6d8,#8cc86a)"></div>
    </div>
    <div class="grid">
      <div class="card"><div class="name">Etiam non auctor</div><div class="stars">★★★★★</div><div class="price">$9.00</div><div class="pimg" role="img" aria-label="Boxed drinks" style="background:linear-gradient(#c8a078,#6a4a2a)"></div><span class="badge">NEW</span></div>
      <div class="card"><div class="name">Aliquam ac lectus</div><div class="stars">★★★★★</div><div class="price">$8.00</div><div class="pimg" role="img" aria-label="Juice bottles" style="background:linear-gradient(#f8e08a,#e8862a)"></div><span class="badge">NEW</span></div>
      <div class="card"><div class="name">Etiam non auctor</div><div class="stars">★★★★★</div><div class="price">$12.00</div><div class="pimg" role="img" aria-label="Wine bottles" style="background:linear-gradient(#6a4a3a,#2a1a14)"></div><span class="badge">NEW</span></div>
      <div class="card"><div class="name">Integer velit mauris</div><div class="stars">★★★★★</div><div class="price">$5.00</div><div class="pimg" role="img" aria-label="Drink cans" style="background:linear-gradient(#e8e8e8,#b03030)"></div><span class="badge">NEW</span></div>
      <div class="card"><div class="name">Aliquam ac lectus</div><div class="stars">★★★★★</div><div class="price">$6.00</div><div class="pimg" role="img" aria-label="Soda bottles" style="background:linear-gradient(#f4c86a,#d8422a)"></div><span class="badge">NEW</span></div>
      <div class="card"><div class="name">Etiam non auctor</div><div class="stars">★★★★★</div><div class="price">$7.00</div><div class="pimg" role="img" aria-label="Mineral water" style="background:linear-gradient(#d8eef8,#6aa8d8)"></div><span class="badge">NEW</span></div>
    </div>
  </div>
</section>

<!-- Specialty Deli -->
<section class="section" style="top:2990px">
  <div class="head-split">
    <div class="sec-head" style="width:750px"><span class="sec-title" style="color:var(--brown)">Specialty Deli</span><div class="tabs"><span>Home</span><span>Cheese</span><span>Meats</span><span>Olives</span><span>Bread</span><span>Salads</span></div></div>
    <div class="tag" style="width:250px;background:var(--brown)">SPECIAL PRODUCTS</div>
  </div>
  <div class="sec-body">
    <div class="grid">
      <div class="card"><div class="name">Maecenas ultricies</div><div class="stars">★★★★★</div><div class="price">$18.00</div><div class="pimg" role="img" aria-label="Sandwich" style="background:linear-gradient(#f0d0a0,#b8783a)"></div><span class="badge">NEW</span></div>
      <div class="card"><div class="name">Etiam non auctor</div><div class="stars">★★★★★</div><div class="price">$15.00</div><div class="pimg" role="img" aria-label="Wraps" style="background:linear-gradient(#f4dcaa,#c08a4a)"></div><span class="badge">NEW</span></div>
      <div class="card"><div class="name">Integer velit mauris</div><div class="stars">★★★★★</div><div class="price">$20.00</div><div class="pimg" role="img" aria-label="Baguette roll" style="background:linear-gradient(#eccc8a,#a86a2a)"></div><span class="badge">NEW</span></div>
      <div class="card"><div class="name">Nam vulputate magna</div><div class="stars">★★★★★</div><div class="price">$22.00</div><div class="pimg" role="img" aria-label="Cheese platter" style="background:linear-gradient(#fbe6a0,#d8a83a)"></div><span class="badge">NEW</span></div>
      <div class="card"><div class="name">Curabitur tristique</div><div class="stars">★★★★★</div><div class="price">$16.00</div><div class="pimg" role="img" aria-label="Salad bowl" style="background:linear-gradient(#c8e49a,#6a9a3a)"></div><span class="badge">NEW</span></div>
      <div class="card"><div class="name">Lorem ipsum dolor</div><div class="stars">★★★★★</div><div class="price">$19.00</div><div class="pimg" role="img" aria-label="Deli meats" style="background:linear-gradient(#f0a88a,#b0422a)"></div><span class="badge">NEW</span></div>
    </div>
    <div class="promo" style="background:linear-gradient(#8a6a54,#5a3e2e)">
      <div class="pt"><div class="a">FOOD</div><div class="b">LOVERS</div><div class="c">Fresh deli every day</div></div>
      <div class="ph" role="img" aria-label="Slice of toasted bread" style="background:linear-gradient(#f0c880,#a8682a)"></div>
    </div>
    <div class="list">
      <div class="li"><div class="th" role="img" aria-label="Bagel sandwich" style="background:linear-gradient(#f0d0a0,#b8783a)"></div><div><div class="name">Nam vulputate magna</div><div class="stars">★★★★★</div><div class="price">$14.00</div></div></div>
      <div class="li"><div class="th" role="img" aria-label="Pastry" style="background:linear-gradient(#f4dcaa,#c08a4a)"></div><div><div class="name">Maecenas ultricies</div><div class="stars">★★★★★</div><div class="price">$9.00</div></div></div>
      <div class="li"><div class="th" role="img" aria-label="Sub roll" style="background:linear-gradient(#eccc8a,#a86a2a)"></div><div><div class="name">Curabitur tristique</div><div class="stars">★★★★★</div><div class="price">$12.00</div></div></div>
      <div class="li"><div class="th" role="img" aria-label="Croissant" style="background:linear-gradient(#f6d890,#c8882a)"></div><div><div class="name">Integer velit mauris</div><div class="stars">★★★★★</div><div class="price">$6.00</div></div></div>
    </div>
  </div>
</section>

<div class="wrap strip">
  <span class="arrow">‹</span>
  <span class="mini"><i></i>BROVAN MARKET</span>
  <span class="mini"><i></i>BROVAN MARKET</span>
  <span class="mini"><i></i>BROVAN MARKET</span>
  <span class="arrow">›</span>
</div>

<div class="newsletter"><b>NEWSLETTER SIGN UP</b><div class="in">Your email address</div><div class="btn">SUBSCRIBE</div></div>

<footer class="footer">
  <div class="cols">
    <div class="col" style="flex:1.4"><div class="foot-brand"><i></i><span>BROVAN MARKET</span></div>Your local grocer, delivered to your door every week.</div>
    <div class="col"><h4>MY ACCOUNT</h4>My Orders<br>My Wishlist<br>Addresses<br>Personal Info</div>
    <div class="col"><h4>CUSTOMER SERVICE</h4>Shipping<br>Returns<br>Privacy Policy<br>Help &amp; FAQ</div>
    <div class="col"><h4>INFORMATION</h4>About Us<br>Delivery<br>Terms<br>Site Map</div>
    <div class="col"><h4>CONTACT INFO</h4>www.brovanmarket.com.au<br>Open 7 days<br>8am – 9pm</div>
  </div>
</footer>

<div class="social">
  <i style="background:#3b5998"></i><i style="background:#2aa3ef"></i><i style="background:#0a7bb5"></i><i style="background:#3a8f3a"></i><i style="background:#d64a36"></i>
</div>
<div class="totop"></div>

</body>
</html>
```